Finance Company Needs a New Website Design

Looking for a fresh new design, based on logo and wireframes given, to come up with a modern professional look and feel for the company. Note we will award based on the homepage design, but expect the winning designer to deliver the other pages.

Target Market(s)

Large Corporate and Finance Professionals (C-Suite Level)

Industry/Entity Type

Finance / Professional

Number of Pages Required

5+ page

Font styles to use
Sans Serif
Other font styles liked:
• Use Roboto/Open Sans for body/small headings, use Impact for larger headings (like the Brevath website).

Requirements
Must have
• High Attention to Detail. Following the Wireframes closely. High impact and fits well with the Brevath.co.uk website.
Nice to have
• Must fit with the Brevath website look and feel, but be different - so that they cannot be mistaken for each other. Use the arrow motif from the logo carefully.
Should not have
• Anything cheap, too bright or untidy

```html
<!DOCTYPE html>
<html lang="en">
<head>
<meta charset="utf-8">
<title>Keelmark – Sell Your Business</title>
<link rel="stylesheet" href="https://fonts.googleapis.com/css2?family=Outfit:wght@300;400;500;600;700&family=Jost:wght@500;600&family=Nunito+Sans:wght@700;800&display=swap">
<style>
:root{
  --plum:#55215d;
  --plum-dark:#4a1c52;
  --ink:#222;
  --grey:#555;
  --topbar:#4b4b4d;
  --pale:#f0f1f3;
  --navy:#1b2447;
  --navy-deep:#161e3c;
  --white:#fff;
}
*{margin:0;padding:0;box-sizing:border-box}
html,body{width:1200px;height:3019px;overflow:hidden}
body{font-family:"Outfit",sans-serif;color:var(--ink);background:var(--white);position:relative}
.abs{position:absolute}
a{color:inherit;text-decoration:none}

/* header */
.brand-box{left:0;top:0;width:264px;height:112px;background:var(--white);display:flex;align-items:center;justify-content:center}
.brand-name{font-family:"Outfit",sans-serif;font-weight:700;font-size:34px;color:var(--plum);letter-spacing:-1px}
.topbar{left:264px;top:0;width:936px;height:42px;background:var(--topbar);display:flex;align-items:center;justify-content:flex-end;padding-right:34px;gap:26px;color:var(--white);font-size:15px}
.phone{border:1px solid var(--white);padding:1px 12px;display:flex;align-items:center;gap:5px;font-size:14px;margin-left:8px}
.navbar{left:264px;top:42px;width:936px;height:70px;background:var(--pale);display:flex;align-items:center;justify-content:flex-end;padding-right:22px;gap:33px;font-size:15px;color:#333}
.burger{margin-left:20px;display:flex;flex-direction:column;gap:6px}
.burger span{display:block;width:27px;height:3px;background:#444;border-radius:2px}

/* hero */
.hero{left:0;top:112px;width:1200px;height:524px;background:linear-gradient(90deg,#2a2f5b 0%,#3e4a78 40%,#5a6c90 65%,#394258 100%)}
.hero-title{left:38px;top:270px;color:var(--white);font-weight:600;font-size:49px;line-height:56px;letter-spacing:-1.5px}
.btn{display:flex;align-items:center;justify-content:center;gap:10px;font-family:"Nunito Sans",sans-serif;font-weight:800;font-size:14px;letter-spacing:.3px;color:var(--white);border-radius:3px}
.btn-solid{background:var(--plum)}
.btn-line{border:2px solid var(--plum)}

/* intro */
.intro{left:0;top:636px;width:1200px;height:500px;background:var(--pale);text-align:center}
.intro h2{font-family:"Jost",sans-serif;font-weight:500;font-size:32px;color:#444;margin-top:116px;margin-bottom:20px}
.intro p{width:810px;margin:0 auto 17px;font-size:14.5px;line-height:19.5px;color:var(--grey);font-weight:300}

/* acquirers */
.acq-title{left:110px;top:1222px;font-family:"Jost",sans-serif;font-weight:500;font-size:32px;color:#444}
.acq-copy{left:110px;top:1280px;width:485px}
.acq-copy p{font-size:14.5px;line-height:19.5px;color:var(--grey);font-weight:300;margin-bottom:36px}
.photo{border-radius:6px}
.stat{left:657px;top:1635px;width:106px;height:106px;border-radius:50%;background:#4c4c4e;color:var(--white);display:flex;flex-direction:column;align-items:center;justify-content:center;box-shadow:0 8px 18px rgba(0,0,0,.25)}
.stat b{font-size:23px;font-weight:600}
.stat span{font-size:17px}

/* connect */
.connect{left:593px;top:1890px;width:569px;height:555px;background:var(--plum);border-radius:6px;padding:52px 52px 0;color:var(--white)}
.connect h2{font-weight:600;font-size:42px;line-height:50px;letter-spacing:-1.2px;margin-bottom:34px}
.connect p{font-size:14.5px;line-height:19.5px;font-weight:400;margin-bottom:26px}
.btn-white{background:var(--white);color:var(--plum-dark);width:172px;height:52px;border-radius:3px}

/* footer */
.footer{left:0;top:2557px;width:1200px;height:376px;background:var(--navy)}
.fcol{top:2620px}
.fcol h3{font-weight:600;font-size:20px;color:var(--white);margin-bottom:28px;letter-spacing:-.3px}
.fcol li{list-style:none;color:var(--white);font-size:15px;font-weight:300;margin-bottom:17px;display:flex;align-items:center;gap:8px}
.email{left:897px;top:2795px;width:228px;height:49px}
.legal{left:0;top:2933px;width:1200px;height:86px;background:var(--navy-deep);display:flex;align-items:center;justify-content:space-between;padding:0 38px;color:#c9ccd8;font-size:14.5px;font-weight:300}
.legal nav{display:flex;gap:27px}
</style>
</head>
<body>

<header>
  <div class="abs brand-box"><span class="brand-name">keelmark</span></div>
  <div class="abs topbar">
    <a href="#">Insights &amp; News</a><a href="#">About Us</a><a href="#">Contact Us</a>
    <span class="phone"><svg width="12" height="12" viewBox="0 0 24 24"><path fill="#fff" d="M6.6 10.8a15 15 0 0 0 6.6 6.6l2.2-2.2a1 1 0 0 1 1-.25 11.4 11.4 0 0 0 3.6.57 1 1 0 0 1 1 1V20a1 1 0 0 1-1 1A17 17 0 0 1 3 4a1 1 0 0 1 1-1h3.5a1 1 0 0 1 1 1c0 1.25.2 2.45.57 3.57a1 1 0 0 1-.25 1z"/></svg>020 4516 0937</span>
  </div>
  <nav class="abs navbar">
    <a href="#">Sell Your Business</a><a href="#">Valuation</a><a href="#">Work With Us</a>
    <div class="burger"><span></span><span></span><span></span></div>
  </nav>
</header>

<section class="abs hero" role="img" aria-label="Photo of two business advisors smiling while working at a laptop in an office"></section>
<h1 class="abs hero-title">We Find The Best Buyer<br>You Get The Best Exit</h1>
<a class="abs btn btn-solid" style="left:38px;top:421px;width:151px;height:48px" href="#">Read More
  <svg width="13" height="12" viewBox="0 0 13 12"><path d="M1 6h10M7 2l4 4-4 4" stroke="#fff" stroke-width="2" fill="none"/></svg></a>
<a class="abs btn btn-line" style="left:213px;top:421px;width:171px;height:48px" href="#">Our Services
  <svg width="14" height="14" viewBox="0 0 14 14"><circle cx="7" cy="7" r="6" stroke="#fff" stroke-width="1.6" fill="none"/><path d="M4 7h6M7.5 4.5 10 7l-2.5 2.5" stroke="#fff" stroke-width="1.6" fill="none"/></svg></a>

<section class="abs intro">
  <h2>Sell Your Business for more</h2>
  <p>You may have already considered how much your business is worth, or even have received a suggested price for the sale of your business. If you have, then it might be worth considering a very apparent truth.</p>
  <p>Any business valuation you have in mind, or have recieved, is just a number. In many cases, it is not close to what your business may sell for. To wish is one thing, to receive a good offer is much harder.</p>
  <p>Which is why owners choose to work with us. We know that your future business disposal and sale price will be maximised in two ways: by reaching as many of the most likely buyers as possible, and by finding the best fit.</p>
  <p>Only then will you receive the best offer for your business and complete on the dispisal of your company.</p>
</section>

<section>
  <h2 class="abs acq-title">Reach only serious Acquirers</h2>
  <div class="abs acq-copy">
    <p>With access to over 13,000 active acquirers throughout our national and global network, all of whom we have qualified to ensure they have the capabilitis to make good offers for suitable businesses.</p>
    <p>We have partnerships with websites we have evaluated to give us the greatest possible coverage of any additional by=uyers who may be intrested in your company.</p>
    <p>We have a full set of global business data meaning that we can run intensive campaigns to help you get in front of specific trade buyers, and with our office in Sydney, we cover every time zone.</p>
  </div>
  <a class="abs btn btn-solid" style="left:110px;top:1570px;width:174px;height:49px" href="#">Reach Matters
    <svg width="13" height="12" viewBox="0 0 13 12"><path d="M1 6h10M7 2l4 4-4 4" stroke="#fff" stroke-width="2" fill="none"/></svg></a>
  <div class="abs photo" style="left:691px;top:1233px;width:399px;height:492px;background:linear-gradient(160deg,#c9cdd0 0%,#8a7c70 45%,#c9703a 70%,#8fc6c9 100%)" role="img" aria-label="Photo of two colleagues reviewing work on a laptop"></div>
  <div class="abs" style="left:843px;top:1197px;width:220px;height:220px;background:var(--plum);border-radius:3px"></div>
  <div class="abs stat"><b>10k+</b><span>Clients</span></div>
</section>

<section>
  <div class="abs photo" style="left:38px;top:1883px;width:612px;height:569px;background:linear-gradient(120deg,#e9e4de 0%,#c7b3a3 40%,#6e7f98 70%,#3b3a3a 100%)" role="img" aria-label="Photo of a young man and woman working together on a laptop"></div>
  <div class="abs connect">
    <h2>Connect with the best fitting buyers</h2>
    <p>From our research, and having engaged with as many potential acquirers as possible, we will work alongside you to identify the most interesting prospective acquirers.</p>
    <p>In most cases these are the companies with the best fit for your business. It will mean that they will pay a premium foryour business beacuase there is more value.</p>
    <p>Working with you, we will coordinate a competitive process, engaging the most suitable acquirers and their advisors, and ensuring that the offers made exceed expectations, not just in price, but also in terms of your future</p>
    <a class="btn btn-white" href="#">Finding the Fit</a>
  </div>
</section>

<footer>
  <div class="abs footer"></div>
  <svg width="0" height="0" style="position:absolute"><symbol id="tick" viewBox="0 0 12 10"><path d="M1 5l3.5 3.5L11 1.5" stroke="#fff" stroke-width="1.6" fill="none"/></symbol></svg>
  <div class="abs fcol" style="left:73px"><h3>Sell Your Business</h3><ul>
    <li><svg width="12" height="10"><use href="#tick"/></svg>Direct to Market</li>
    <li><svg width="12" height="10"><use href="#tick"/></svg>Maximising Reach</li>
    <li><svg width="12" height="10"><use href="#tick"/></svg>Focus on Fit</li>
    <li><svg width="12" height="10"><use href="#tick"/></svg>Exit Planning</li></ul></div>
  <div class="abs fcol" style="left:359px"><h3>Valuation</h3><ul>
    <li><svg width="12" height="10"><use href="#tick"/></svg>Calculator</li>
    <li><svg width="12" height="10"><use href="#tick"/></svg>Getting the Fit</li>
    <li><svg width="12" height="10"><use href="#tick"/></svg>How to Build Value</li></ul></div>
  <div class="abs fcol" style="left:646px"><h3>Work With Us</h3><ul>
    <li><svg width="12" height="10"><use href="#tick"/></svg>M&amp;A Advisors</li>
    <li><svg width="12" height="10"><use href="#tick"/></svg>Global Coverage</li>
    <li><svg width="12" height="10"><use href="#tick"/></svg>Acquisitions</li></ul></div>
  <div class="abs fcol" style="left:897px"><h3>About Us</h3><ul>
    <li><svg width="12" height="10"><use href="#tick"/></svg>Insights and News</li>
    <li><svg width="12" height="10"><use href="#tick"/></svg>About Us</li>
    <li><svg width="12" height="10"><use href="#tick"/></svg>Contact Us</li></ul></div>
  <a class="abs btn btn-solid email" href="#">Email Us
    <svg width="14" height="11" viewBox="0 0 14 11"><rect width="14" height="11" rx="1" fill="#fff"/><path d="M1 1.5 7 6l6-4.5" stroke="#55215d" stroke-width="1.4" fill="none"/></svg></a>
  <div class="abs legal">
    <span>(c) Keelmark a Trading Name of Brevath Limited. All rights reserved</span>
    <nav><a href="#">Sitemap</a><a href="#">Terms of Use</a><a href="#">Privacy Policy</a><a href="#">Contact Us</a></nav>
  </div>
</footer>

</body>
</html>
```